Electrictrian Contractor Website Design

We are working with an electrical contractor in California called Crest Electric.

Some sites to use for content/competitors and inspiration:
https://tamrinwired.com
https://pravikdesk.surf/web/contractor/ (lots of contractor website designs we've approved and continue to show clients)

Thank you for taking the time to consider designing a website for us. We are web developers based in Stockton, CA, USA. Most of our projects go through the same process. Understanding this process may help you win a project with us. We custom-code all of our websites in-house. We don’t have any requirements as to what tools you use for your design, but we prefer Figma files. For any design that we label as four-stars, we send it to the client for review. The client picks the final design they want us to use. Once we complete this process, we will continue to show additional clients all the four-star sites and purchase them later. Your designs will have multiple chances to sell. For better chances of success, we ask that you follow these guidelines.

IMAGES:
If you use any images or icons in the design, we ask that you have a link to the asset so we can purchase the image/icon. Most of the designs we submit do not have the customer’s images on them unless they have some great images. Be creative; show us the feeling you are trying to portray with your image choices. Use any royalty-free site you choose. We subscribe to Quillo and mainly use their images, but we can purchase images outside of Quillo.

PLEASE NOTE: we will not submit designs to clients with watermarks on the images.

FONTS:
We ask that you identify the fonts used in the design. This can be done in a message if you want. We typically use Google Fonts and Quillo Fonts.

CONTENT:
We're always open to different content and ideas. We often submit designs with stock images so the client can see our vision. We typically take pictures after the website launch to use their images with our vision. Lorem Ipsum is fine for paragraphs, but we ask that you write the headers in correct English. We want to be able to show the vision and identify the sections of the website.

INSPIRATION:
We typically add a couple of links in the brief of websites we like to help you get started in your design.

REVISIONS:
We do not often ask for revisions of the designs unless we see something in the design that may not appeal to the client. If there are slight changes that we want to make, we do that in the development process.

FEEDBACK:
We rarely give feedback on designs during the design process. We are working on many website projects and do not have the time to provide feedback. We usually respond if your request is well thought out and asks specific questions, but a note asking “feedback, please” usually goes unanswered

```html
<!DOCTYPE html>
<html lang="en">
<head>
<meta charset="utf-8">
<title>Crest Electric</title>
<link href="https://fonts.googleapis.com/css2?family=Montserrat:wght@400;500;600;700;800&display=swap" rel="stylesheet">
<style>
:root{
  --navy:#1b4a98;
  --navy-dark:#153c80;
  --yellow:#f8b70f;
  --ink:#222;
  --muted:#555;
  --pale:#eef3fb;
  --white:#fff;
  --field:#f1f1f1;
}
*{box-sizing:border-box;margin:0;padding:0}
html,body{width:1200px;height:5263px;overflow:hidden}
body{font-family:"Montserrat",sans-serif;color:var(--ink);background:var(--white);position:relative}
section,header,footer{position:absolute;left:0;width:1200px}
.photo{position:absolute}
.btn{position:absolute;display:flex;align-items:center;justify-content:center;gap:14px;border-radius:40px;font-weight:700;color:var(--white);background:var(--navy);text-transform:uppercase}
.btn .arrow{width:20px;height:20px;border-radius:50%;background:var(--white);display:inline-flex;align-items:center;justify-content:center}
.btn .arrow svg{width:12px;height:12px}
.section-title{position:absolute;left:0;width:1200px;text-align:center;font-size:46px;font-weight:700;color:var(--navy)}
.rule{position:absolute;height:3px;background:var(--yellow)}
p.lorem{font-size:12px;line-height:21px;color:var(--muted)}

/* wordmark */
.brand{position:absolute;display:flex;align-items:center;gap:12px;font-size:27px;font-weight:700;color:var(--navy);white-space:nowrap}
.brand .dot{width:22px;height:22px;border-radius:50%;background:var(--yellow);flex:none}

/* header */
.site-header{top:0;height:112px}
.site-header .brand{left:66px;top:38px}
.topbar{position:absolute;left:388px;top:0;width:812px;height:38px;background:var(--yellow);border-bottom-left-radius:30px;display:flex;justify-content:flex-end;align-items:center;gap:22px;padding-right:64px;font-size:11px;color:var(--white);font-weight:600}
.topbar span{display:flex;align-items:center;gap:8px}
.topbar i{width:26px;height:26px;border-radius:50%;background:var(--navy);display:inline-flex;align-items:center;justify-content:center}
.nav{position:absolute;right:64px;top:62px;display:flex;gap:29px;font-size:11px;font-weight:500;color:#333}
.nav .active{color:var(--navy);border-bottom:2px solid var(--navy);padding-bottom:6px}

/* hero */
.hero{top:112px;height:659px;background:linear-gradient(90deg,#fff 0%,#f4f4f4 50%)}
.hero h1{position:absolute;left:64px;top:125px;font-size:48px;line-height:64px;font-weight:500;color:var(--navy)}
.hero h1 b{font-weight:800}
.dots{position:absolute;left:570px;top:586px;display:flex;gap:4px}
.dots i{width:10px;height:10px;border-radius:50%;background:#9fb2d2}
.dots i:first-child{background:var(--navy)}

/* stats */
.stats{top:771px;height:346px;background:var(--navy)}
.stat{position:absolute;top:96px;width:200px;text-align:center;color:var(--white)}
.stat .ring{width:118px;height:118px;margin:0 auto;border-radius:50%;border:2px dashed var(--yellow);display:flex;align-items:center;justify-content:center}
.stat .ring div{width:104px;height:104px;border-radius:50%;background:var(--yellow);display:flex;align-items:center;justify-content:center;font-size:30px;font-weight:500}
.stat h4{margin-top:26px;font-size:15px;font-weight:700}

/* services */
.services{top:1117px;height:1293px}
.card{position:absolute;width:521px;height:453px;background:var(--white);box-shadow:0 2px 12px rgba(0,0,0,.14);text-align:center}
.card .photo{left:0;top:0;width:521px;height:227px}
.card h3{position:absolute;top:257px;width:100%;font-size:23px;font-weight:500;color:var(--navy)}
.card p{position:absolute;top:300px;left:28px;right:28px}
.card .btn{left:196px;top:381px;width:130px;height:36px;font-size:10px}

/* about */
.about{top:2410px;height:555px;background:var(--pale)}
.about .frame{position:absolute;left:135px;top:83px;width:330px;height:355px;border:3px solid var(--yellow)}
.about h2{position:absolute;left:563px;top:106px;font-size:34px;font-weight:700;color:var(--navy)}
.about p{position:absolute;left:563px;top:192px;width:502px;font-size:12px;line-height:28px;color:#333;text-align:justify}
.about .btn{left:563px;top:400px;width:146px;height:42px;font-size:11px}

/* cta */
.cta{top:2965px;height:478px;background:linear-gradient(90deg,#1b4a98,#1f4f9e 60%,#2a5aa6)}
.cta h2{position:absolute;top:80px;width:100%;text-align:center;font-size:62px;line-height:84px;font-weight:600;color:var(--white)}
.cta h2 span{color:var(--yellow);font-weight:800;font-size:72px}
.cta .rule{left:550px;top:263px;width:100px;background:var(--white);height:2px}
.cta .btn{left:470px;top:317px;width:260px;height:70px;background:var(--yellow);font-size:22px}
.cta .btn .arrow{width:26px;height:26px;background:var(--navy)}

/* projects */
.projects{top:3443px;height:867px}
.project{position:absolute;top:227px;width:312px}
.project .photo{left:0;top:0;width:312px;height:260px}
.project h3{position:absolute;top:297px;font-size:19px;font-weight:700;color:var(--navy);white-space:nowrap}
.project p{position:absolute;top:335px;width:300px}
.project a{position:absolute;top:390px;font-size:12px;font-weight:700;color:var(--yellow);text-decoration:underline}
.projects .more{left:488px;top:697px;width:224px;height:72px;font-size:19px}

/* contact */
.contact{top:4310px;height:595px}
.contact h2{position:absolute;left:160px;top:126px;font-size:34px;font-weight:700;color:var(--navy)}
.field{position:absolute;background:var(--field);font-size:10px;color:#888;padding:14px 18px}
.contact .btn{left:163px;top:480px;width:160px;height:42px;font-size:11px}
.contact .frame{position:absolute;left:680px;top:96px;width:360px;height:400px;border:3px solid var(--yellow)}
.contact .photo{left:662px;top:116px;width:360px;height:398px}

/* footer */
.site-footer{top:4905px;height:358px;background:var(--navy-dark);color:var(--white)}
.site-footer .brand{color:var(--white);left:66px;top:172px;font-size:25px}
.site-footer h5{position:absolute;top:88px;font-size:19px;font-weight:600;border-bottom:2px solid var(--yellow);padding-bottom:2px}
.links{position:absolute;top:151px;list-style:none;font-size:13px;line-height:26px}
.links li::before{content:"";display:inline-block;width:9px;height:9px;border-radius:50%;background:var(--yellow);margin-right:12px}
.cinfo{position:absolute;left:662px;font-size:13px;line-height:15px;display:flex;gap:16px}
.cinfo i{width:21px;height:21px;background:var(--yellow);border-radius:4px;flex:none;display:inline-flex;align-items:center;justify-content:center}
.news p{position:absolute;left:937px;top:150px;width:200px;font-size:13px;line-height:16px}
.news .input{position:absolute;left:937px;top:195px;width:196px;height:30px;background:var(--white)}
.news .sub{position:absolute;left:937px;top:238px;width:100px;height:28px;background:var(--yellow);font-size:9px;font-weight:700;display:flex;align-items:center;justify-content:center}
.copyright{position:absolute;left:66px;top:330px;font-size:11px}
.social{position:absolute;left:1013px;top:325px;display:flex;gap:6px}
.social i{width:24px;height:24px;background:var(--yellow);border-radius:3px}
</style>
</head>
<body>

<header class="site-header">
  <div class="brand"><span class="dot"></span>Crest Electric</div>
  <div class="topbar">
    <span><i><svg width="13" height="13" viewBox="0 0 24 24" fill="#fff"><path d="M6.6 10.8a15 15 0 006.6 6.6l2.2-2.2a1 1 0 011-.25 11.4 11.4 0 003.6.57 1 1 0 011 1V20a1 1 0 01-1 1A17 17 0 013 4a1 1 0 011-1h3.5a1 1 0 011 1 11.4 11.4 0 00.57 3.6 1 1 0 01-.25 1z"/></svg></i>0012 555 0148</span>
    <span><i><svg width="13" height="13" viewBox="0 0 24 24"><path d="M3 6h18v12H3z M3 6l9 7 9-7" stroke="#fff" stroke-width="2" fill="none"/></svg></i>info@crestelectric.com</span>
  </div>
  <nav class="nav">
    <span class="active">HOME</span><span>ABOUT US</span><span>SERVICES ▾</span><span>PROJECTS</span><span>CAREERS</span><span>CAPABILITIES</span><span>COMMUNITY</span><span>CONTACT US</span>
  </nav>
</header>

<section class="hero">
  <div class="photo" role="img" aria-label="Electrician in hard hat and safety glasses wiring a breaker panel" style="left:606px;top:0;width:594px;height:659px;background:linear-gradient(120deg,#c9ccd2 0%,#e6e7ea 45%,#8d8a86 70%,#3c3b3b 100%)"></div>
  <h1><b>Reliability, Quality</b><br>and <b>Expertise</b> in<br>Electrical and General<br>Engineering</h1>
  <div class="btn" style="left:66px;top:426px;width:262px;height:72px;font-size:22px;font-weight:600">Contact Us <span class="arrow"><svg viewBox="0 0 12 12"><path d="M2 6h8M7 3l3 3-3 3" stroke="#1b4a98" stroke-width="1.8" fill="none"/></svg></span></div>
  <div class="dots"><i></i><i></i><i></i></div>
</section>

<section class="stats">
  <div class="stat" style="left:172px"><div class="ring"><div>2009</div></div><h4>YEAR OF FOUNDATION</h4></div>
  <div class="stat" style="left:418px"><div class="ring"><div>+3500</div></div><h4>FINALIZED PROJECTS</h4></div>
  <div class="stat" style="left:648px"><div class="ring"><div>+2100</div></div><h4>CAREER CLIENTS</h4></div>
  <div class="stat" style="left:854px"><div class="ring"><div>+100</div></div><h4>AWARRDS WON</h4></div>
</section>

<section class="services">
  <h2 class="section-title" style="top:118px">OUR SERVICES</h2>
  <div class="rule" style="left:547px;top:183px;width:106px"></div>

  <div class="card" style="left:66px;top:248px">
    <div class="photo" role="img" aria-label="Electrician in hi-vis jacket testing a distribution board" style="background:linear-gradient(90deg,#c7c9a0,#5a6a5e 55%,#9aa0a4)"></div>
    <h3>COMMERCIAL</h3>
    <p class="lorem">Lorem ipsum dolor sit amet, consectetur adipiscing elit. Praesent erat sem, placerat at placerat a, facilisis eget mauris. Nunc luctus nunc lorem, ac posu ere sem feugiat eu. Aliquam non purus commodo.</p>
    <div class="btn">Read More <span class="arrow"><svg viewBox="0 0 12 12"><path d="M2 6h8M7 3l3 3-3 3" stroke="#1b4a98" stroke-width="1.8" fill="none"/></svg></span></div>
  </div>
  <div class="card" style="left:614px;top:248px">
    <div class="photo" role="img" aria-label="Industrial factory floor with orange machinery" style="background:linear-gradient(180deg,#b9bcbf,#7c8185 60%,#b5563a 80%,#d5d5d5)"></div>
    <h3>INDUSTRIAL &amp; AGRICULTURE</h3>
    <p class="lorem">Lorem ipsum dolor sit amet, consectetur adipiscing elit. Praesent erat sem, placerat at placerat a, facilisis eget mauris. Nunc luctus nunc lorem, ac posu ere sem feugiat eu. Aliquam non purus commodo.</p>
    <div class="btn">Read More <span class="arrow"><svg viewBox="0 0 12 12"><path d="M2 6h8M7 3l3 3-3 3" stroke="#1b4a98" stroke-width="1.8" fill="none"/></svg></span></div>
  </div>
  <div class="card" style="left:66px;top:728px">
    <div class="photo" role="img" aria-label="Lit underground rail tunnel" style="background:radial-gradient(circle at 50% 60%,#f3e1b0 0%,#a86a2e 25%,#3a2616 60%,#1a120c 100%)"></div>
    <h3>UNDERGROUND AND CIVIL WORK</h3>
    <p class="lorem">Lorem ipsum dolor sit amet, consectetur adipiscing elit. Praesent erat sem, placerat at placerat a, facilisis eget mauris. Nunc luctus nunc lorem, ac posu ere sem feugiat eu. Aliquam non purus commodo.</p>
    <div class="btn">Read More <span class="arrow"><svg viewBox="0 0 12 12"><path d="M2 6h8M7 3l3 3-3 3" stroke="#1b4a98" stroke-width="1.8" fill="none"/></svg></span></div>
  </div>
  <div class="card" style="left:614px;top:728px">
    <div class="photo" role="img" aria-label="Two workers in hard hats discussing plans at a building site" style="background:linear-gradient(90deg,#8a6f58,#d9d4cb 45%,#c9c4bb 70%,#eee)"></div>
    <h3>MULTIFAMILY / RESIDENTIAL</h3>
    <p class="lorem">Lorem ipsum dolor sit amet, consectetur adipiscing elit. Praesent erat sem, placerat at placerat a, facilisis eget mauris. Nunc luctus nunc lorem, ac posu ere sem feugiat eu. Aliquam non purus commodo.</p>
    <div class="btn">Read More <span class="arrow"><svg viewBox="0 0 12 12"><path d="M2 6h8M7 3l3 3-3 3" stroke="#1b4a98" stroke-width="1.8" fill="none"/></svg></span></div>
  </div>
</section>

<section class="about">
  <div class="frame"></div>
  <div class="photo" role="img" aria-label="Technician working on cabled electrical cabinet" style="left:153px;top:99px;width:328px;height:362px;background:linear-gradient(90deg,#2d3c5c,#1d2436 40%,#6d7480 70%,#c7cacd)"></div>
  <h2>ABOUT US</h2>
  <p>Lorem ipsum dolor sit amet, consectetur adipiscing elit. Etiam in vestibu lum urna. Quisque in lectus non sem consequat varius mattis id odio. Mauris sed libero a velit pellentesque volutpat. Donec sed augue congue, consequat eros in, fringilla ante. Interdum et malesuada fames ac ante ipsum primis in faucibus. Lorem ipsum dolor sit amet, consecte tur adipiscing elit. Etiam in vestibulum urna.</p>
  <div class="btn">Read More <span class="arrow"><svg viewBox="0 0 12 12"><path d="M2 6h8M7 3l3 3-3 3" stroke="#1b4a98" stroke-width="1.8" fill="none"/></svg></span></div>
</section>

<section class="cta">
  <h2>Let's power the<br><span>future together!</span></h2>
  <div class="rule"></div>
  <div class="btn">Contact Us <span class="arrow"><svg viewBox="0 0 12 12"><path d="M2 6h8M7 3l3 3-3 3" stroke="#fff" stroke-width="1.8" fill="none"/></svg></span></div>
</section>

<section class="projects">
  <h2 class="section-title" style="top:136px">OUR PROJECTS</h2>
  <div class="rule" style="left:550px;top:199px;width:100px"></div>

  <div class="project" style="left:92px">
    <div class="photo" role="img" aria-label="Electrician holding a tablet beside a breaker panel" style="background:linear-gradient(90deg,#8fa0b4,#40464f 55%,#d5d6d8)"></div>
    <h3>Lorem ipsum dolor sit amet</h3>
    <p class="lorem">Lorem ipsum dolor sit amet, consectetur adip iscing elit. Praesent erat sem, placerat .</p>
    <a>READ MORE</a>
  </div>
  <div class="project" style="left:443px">
    <div class="photo" role="img" aria-label="Electrician with safety glasses adjusting panel wiring" style="background:linear-gradient(90deg,#b9b6b0,#6d6a66 50%,#c4c5c7)"></div>
    <h3>Lorem ipsum dolor sit amet</h3>
    <p class="lorem">Lorem ipsum dolor sit amet, consectetur adip iscing elit. Praesent erat sem, placerat .</p>
    <a>READ MORE</a>
  </div>
  <div class="project" style="left:795px">
    <div class="photo" role="img" aria-label="Electrician in orange hard hat on a ladder at a switchboard" style="background:linear-gradient(90deg,#bcc0c6,#3c3f44 50%,#d6d7d9)"></div>
    <h3>Lorem ipsum dolor sit amet</h3>
    <p class="lorem">Lorem ipsum dolor sit amet, consectetur adip iscing elit. Praesent erat sem, placerat .</p>
    <a>READ MORE</a>
  </div>

  <div class="btn more">View More <span class="arrow"><svg viewBox="0 0 12 12"><path d="M2 6h8M7 3l3 3-3 3" stroke="#1b4a98" stroke-width="1.8" fill="none"/></svg></span></div>
</section>

<section class="contact">
  <h2>CONTACT US</h2>
  <div class="field" style="left:161px;top:212px;width:199px;height:40px">First Name:</div>
  <div class="field" style="left:377px;top:212px;width:199px;height:40px">Last Name:</div>
  <div class="field" style="left:161px;top:270px;width:199px;height:40px">Phone:</div>
  <div class="field" style="left:377px;top:270px;width:199px;height:40px">Email:</div>
  <div class="field" style="left:161px;top:328px;width:415px;height:128px;padding-top:28px">Mesage:</div>
  <div class="btn">Submit Now <span class="arrow"><svg viewBox="0 0 12 12"><path d="M2 6h8M7 3l3 3-3 3" stroke="#1b4a98" stroke-width="1.8" fill="none"/></svg></span></div>
  <div class="frame"></div>
  <div class="photo" role="img" aria-label="Electrician in white hard hat checking a control panel" style="background:linear-gradient(90deg,#9aa3ae,#cfd2d6 50%,#2f3237 80%,#d8d9db)"></div>
</section>

<footer class="site-footer">
  <div class="brand"><span class="dot"></span>Crest Electric</div>

  <h5 style="left:345px">Quick Links</h5>
  <ul class="links" style="left:345px"><li>Home</li><li>About</li><li>Our Services</li><li>Projects</li></ul>
  <ul class="links" style="left:488px"><li>Careers</li><li>Capabilities</li><li>Community</li><li>Contact Us</li></ul>

  <h5 style="left:662px">Contact Us</h5>
  <div class="cinfo" style="top:153px"><i><svg width="11" height="11" viewBox="0 0 24 24" fill="#153c80"><path d="M6.6 10.8a15 15 0 006.6 6.6l2.2-2.2a1 1 0 011-.25 11.4 11.4 0 003.6.57 1 1 0 011 1V20a1 1 0 01-1 1A17 17 0 013 4a1 1 0 011-1h3.5a1 1 0 011 1 11.4 11.4 0 00.57 3.6 1 1 0 01-.25 1z"/></svg></i><div>CALL US<br>012-555-0148</div></div>
  <div class="cinfo" style="top:197px"><i><svg width="11" height="11" viewBox="0 0 24 24"><path d="M3 6h18v12H3z M3 6l9 7 9-7" stroke="#153c80" stroke-width="2.5" fill="none"/></svg></i><div>EMAIL US<br>info@crestelectric.com</div></div>
  <div class="cinfo" style="top:243px"><i><svg width="11" height="11" viewBox="0 0 24 24" fill="#153c80"><path d="M12 2a7 7 0 00-7 7c0 5 7 13 7 13s7-8 7-13a7 7 0 00-7-7zm0 9.5A2.5 2.5 0 1112 6a2.5 2.5 0 010 5.5z"/></svg></i><div>Address line dummy here<br>Address line dummy here</div></div>

  <h5 style="left:937px">Our Newsletter</h5>
  <div class="news"><p>Subscribe our newsletter to get the latest news.</p><div class="input"></div><div class="sub">SUBSCRIBE</div></div>

  <div class="copyright">Copyright © 2024 All Rights Reserved By Company name</div>
  <div class="social"><i></i><i></i><i></i><i></i></div>
</footer>

</body>
</html>
```